Web Design Pell Marrow

• An Overview of Pell Marrow for reference: We use to be a component manufacturing company. We sold to customers in USA and manage the builds in China using many manufacturing partners. We had a web site that served this market but we have transitioned over the last several years into “A unique design, development and program management company” It is this message we want to put up on the web now. We provide the design support, we help develop and test a new product for our customers and we provide the manufactured produce once we have transitioned it into production.
• The Target Market: Our customers are all high tech. Each product we produce is custom designed and sold only to one a specific customer. We work with a limited number of customer and sell to new customers by word of mouth and referrals. The web site is to provide a back ground check of any new referral so they can see who we are and our basic capabilities. It is not designed to sell customers or to find new customers but provide a background check to new potential customers.
• Pages Required: We estimate 12:
o Home/Title page is page 1 of PDF. It would have buttons to select other pages
o Names of other pages would be (short titles below if on button, if pull down menu the full title of slide)
 USA Facilities
 China Facilities
 Enclosures
 Antennas
 Connectors
 Cables
 EMI Shields
 Overlays
 Process Development
 Voxtrel
 Contact Us (???) >> new page which we are not sure if we should or should not add.
• Design Specifics; attached is our logo, a PDF and PowerPoint slides showing the views we desire. We like these layouts, but perhaps a better one may be suggested for some artistic reason or layout. It should be clean, simple and user intuitive. We like the off white background and use for most of our presentations. One should be able to go from any screen to any other screen. The quote must include both design and implementation onto our web site which is http://pellmarrowsystems.com/
• Design Process:
We would like to see concepts of the Landing/Homepage, and an internal page initially. Feedback will be provided and you will be asked to continue if your layout is on the correct track.

• Implementation: Desire designer/implimentor to set up on their server. Allow us to test and edit on their site. We will provide password for implementation on our site after final approval.

Target Market(s)

• The Target Market: see above task descripiton

Industry/Entity Type

It Company

Requirements
Must have
• • Pages Required: We estimate 12:
 USA Facilities
 China Facilities
 Enclosures
 Antennas
 Connectors
 Cables
 EMI Shields
 Overlays
 Process Development
 Voxtrel

Must have the implementation phase include in quote. see task description above
Should not have
• Should not be complex or long time loading.
Do not want any twitter or promotional add on functions.

```html
<!DOCTYPE html>
<html lang="en">
<head>
<meta charset="utf-8">
<title>Pell Marrow Technologies</title>
<link href="https://fonts.googleapis.com/css2?family=Arimo:wght@400;700&display=swap" rel="stylesheet">
<style>
:root{
  --blue:#0b6cb8;
  --blue-dark:#095ea1;
  --page:#ffffff;
  --panel:#f0f1f1;
  --text:#666a6e;
  --ink:#111;
  --muted:#9a9a9a;
  --btn-top:#7fb6df;
  --btn-bot:#3f8cc8;
}
*{margin:0;padding:0;box-sizing:border-box}
html,body{width:1020px;height:1200px;overflow:hidden;background:var(--page)}
body{font-family:"Arimo",Arial,sans-serif;color:var(--text);position:relative}
.site{position:absolute;left:82px;top:0;width:857px;height:1200px}

.brand{position:absolute;left:0;right:0;top:22px;display:flex;justify-content:center;align-items:center;gap:8px}
.brand-mark{width:22px;height:22px;background:var(--blue)}
.brand-name{font-weight:700;font-size:26px;color:var(--blue);letter-spacing:.5px}

.main-nav{position:absolute;top:105px;left:0;width:857px;height:39px;background:var(--blue);display:flex;justify-content:space-between;align-items:center;padding:0 10px}
.main-nav a{color:#fff;font-weight:700;font-size:10.5px;text-decoration:none}

.hero{position:absolute;top:144px;left:0;width:857px;height:351px;overflow:hidden;
  background:linear-gradient(90deg,#eef0f2 0%,#f6f4f0 20%,#e9ecef 45%,#f3f5f7 70%,#fbfbfb 100%)}
.hero-photo{position:absolute;left:128px;top:0;width:430px;height:351px;
  background:linear-gradient(180deg,#d9dde2 0%,#c9cfd6 45%,#3a3f47 75%,#2b2f36 100%);opacity:.55}
.hero-copy{position:absolute;right:36px;top:121px;text-align:right;width:300px}
.hero-title{font-size:20px;line-height:25px;font-weight:700;color:var(--blue);text-transform:uppercase}
.hero-text{margin-top:16px;font-size:10.5px;line-height:15px;color:#666}
.hero-dots{display:flex;justify-content:flex-end;gap:3px;margin-top:12px;padding-right:4px}
.hero-dots span{width:9px;height:7px;background:#a9aaab}

.welcome{position:absolute;top:498px;left:0;width:857px;height:137px;background:var(--panel)}
.welcome h2{position:absolute;left:30px;top:18px;font-size:12.5px;color:var(--blue);font-weight:700}
.welcome p{position:absolute;left:30px;top:42px;width:635px;font-size:11px;line-height:18px}
.welcome p a,.latest a{color:var(--ink);text-decoration:none}
.welcome-photo{position:absolute;left:707px;top:23px;width:136px;height:91px;
  background:linear-gradient(90deg,#cfd6dd,#eef0f2 50%,#9aa4ae)}

.services{position:absolute;top:645px;left:0;width:857px;height:268px;background:var(--blue)}
.service{position:absolute;top:0;width:170px}
.service h3{margin-top:16px;font-size:15px;color:#fff;font-weight:700;text-transform:uppercase;white-space:nowrap}
.service-photo{margin-top:7px;width:159px;height:88px}
.service p{margin-top:19px;font-size:11px;line-height:14px;color:#fff}
.btn{position:absolute;top:216px;width:74px;height:20px;border-radius:3px;
  background:linear-gradient(var(--btn-top),var(--btn-bot));border:1px solid #a6cdea;
  color:#fff;font-size:9px;font-weight:700;text-align:center;line-height:18px;text-decoration:none}

.latest{position:absolute;top:936px;left:30px;width:520px}
.latest h2,.what-we-do h2{font-size:12.5px;color:var(--blue);font-weight:700}
.latest p{margin-top:18px;font-size:11px;line-height:17px}
.latest .more{display:block;margin-top:0;font-size:11px;line-height:17px}

.what-we-do{position:absolute;top:936px;left:571px;width:270px}
.what-we-do ul{list-style:none;margin-top:18px}
.what-we-do li{font-size:11px;line-height:17px;color:var(--blue);padding-left:17px;position:relative}
.what-we-do li::before{content:"»";position:absolute;left:0;color:#333}

.footer-rule{position:absolute;top:1114px;left:0;width:857px;height:3px;background:var(--blue)}
.legal{position:absolute;top:1141px;left:31px;font-size:10px;line-height:12px;color:var(--muted);text-transform:uppercase}
.social{position:absolute;top:1138px;left:746px;display:flex;gap:3px}
.social span{width:28px;height:28px;border-radius:2px}
.social .s1{background:#d8231f}
.social .s2{background:#4fa9dd}
.social .s3{background:#2c4d8c}
</style>
</head>
<body>
<div class="site">
  <header class="brand">
    <span class="brand-mark"></span>
    <span class="brand-name">Pell Marrow</span>
  </header>

  <nav class="main-nav">
    <a href="#">Home</a><a href="#">USA Facilities</a><a href="#">China Facilities</a><a href="#">Enclosures</a><a href="#">Antennas</a><a href="#">Connectors</a><a href="#">Cables</a><a href="#">EMI Shields</a><a href="#">Overlays</a><a href="#">Process Development</a><a href="#">Voxtrel</a><a href="#">Contact us</a>
  </nav>

  <section class="hero">
    <div class="hero-photo" role="img" aria-label="Smiling businessman in a bright, blurred office"></div>
    <div class="hero-copy">
      <h1 class="hero-title">A unique design<br>development and<br>program management<br>company</h1>
      <p class="hero-text">Sed ut perspiciatis unde omnis iste natus error sit<br>voluptatem accusantium doloremque laudantium</p>
      <div class="hero-dots"><span></span><span></span><span></span><span></span><span></span></div>
    </div>
  </section>

  <section class="welcome">
    <h2>WELCOME TO OUR COMPANY</h2>
    <p>Sed ut perspiciatis unde omnis iste natus error sit voluptatem accusantium doloremque laudantium, totam rem eaque ipsa quae ab illo inventore veritatis et quasi architecto beatae vitae dicta sunt explicabo. Nemo enim ipvoluptatem quia voluptas sit aspernatur aut odit aut fugit, sed quia consequuntur magni dolores eos qui ration<br>voluptatem sequi nesciunt.<a href="#">Read more..</a></p>
    <div class="welcome-photo" role="img" aria-label="Business team standing in an office"></div>
  </section>

  <section class="services">
    <div class="service" style="left:35px">
      <h3>Enclosure Design</h3>
      <div class="service-photo" role="img" aria-label="Engineers inspecting red enclosures on a workbench" style="background:linear-gradient(135deg,#7d8a7a,#c9c3b8 50%,#c8333a)"></div>
      <p>Sed ut perspiciatis unde omnis iste natus error sit voluptatem laudantium totam rem eaque ipsa quae ab illo</p>
    </div>
    <a class="btn" href="#" style="left:35px">Read more »</a>

    <div class="service" style="left:242px">
      <h3>Antenna Design</h3>
      <div class="service-photo" role="img" aria-label="Technician working at an antenna test bench" style="background:linear-gradient(135deg,#d9dcdc,#8e9593 55%,#3a4d55)"></div>
      <p>Sed ut perspiciatis unde omnis iste natus error sit voluptatem laudantium totam rem eaque ipsa quae ab illo</p>
    </div>
    <a class="btn" href="#" style="left:242px">Read more »</a>

    <div class="service" style="left:451px">
      <h3>Connectors Design</h3>
      <div class="service-photo" role="img" aria-label="Engineers in a blue anechoic test chamber" style="background:linear-gradient(135deg,#1b4f93,#3d78be 60%,#c9c6cc)"></div>
      <p>Sed ut perspiciatis unde omnis iste natus error sit voluptatem laudantium totam rem eaque ipsa quae ab illo</p>
    </div>
    <a class="btn" href="#" style="left:451px">Read more »</a>

    <div class="service" style="left:673px">
      <h3>Membrane Design</h3>
      <div class="service-photo" role="img" aria-label="Close-up of a clear membrane keypad tray" style="background:linear-gradient(135deg,#6d7275,#c4c8ca 50%,#8b9093)"></div>
      <p>Sed ut perspiciatis unde omnis iste natus error sit voluptatem laudantium totam rem eaque ipsa quae ab illo</p>
    </div>
    <a class="btn" href="#" style="left:673px">Read more »</a>
  </section>

  <section class="latest">
    <h2>LATEST TECHNOLOGIES</h2>
    <p>Sed ut perspiciatis unde omnis iste natus error sit voluptatem accusantium doloremque laudantium, totam rem eaque ipsa quae ab illo inventore veritatis et quasi architecto beatae vitae dicta sunt explicabo. Nemo enim ipvoluptatem quia voluptas sit aspernatur aut odit aut fugit, sed quia consequuntur magni dolores eos qui rationvoluptatem sequi nesciunt.</p>
    <a class="more" href="#">Read more..</a>
  </section>

  <section class="what-we-do">
    <h2>WHAT WE DO</h2>
    <ul>
      <li>Custom Enclosure Design &amp; Development</li>
      <li>Custom Antenna Design &amp; Development</li>
      <li>Custom Connecttors Design &amp; Development</li>
      <li>Custom Membrane Switch Designs</li>
      <li>Custom Cable Assembly Design</li>
      <li>Custom SMT PCB EMI Shield Walls</li>
    </ul>
  </section>

  <div class="footer-rule"></div>
  <footer class="legal">
    Copyright 2013. All rights reserved.<br>
    Terms &amp; Conditions &nbsp;- &nbsp; Privacy &nbsp; - &nbsp; Disclaimer
  </footer>
  <div class="social" aria-label="Social links">
    <span class="s1"></span><span class="s2"></span><span class="s3"></span>
  </div>
</div>
</body>
</html>
```